Business card design for a dynamic IT consulting company

We need a business card design for a young firm, specialized in the Telecommunications/Consulting industry. The name of the company is Brask and Partners Business Consulting Ltd. (Short name: Brask and Partnes)
Brask = solve read reverse, so we aim to be uncomplicated and solution-oriented. The small pipe in our logo is also related to the word solve. So we need a new business card design, which is simple, eye catching and something non traditional (I would probably prefer a square shaped design rather than a rectangle, but open for suggestions). Attached our logo.

Target Market(s)

Usually our customers are Tier1 Telecoms providers (Q-Linkra, Parnexo, etc) and their executives.

Industry/Entity Type

Business

Contact Information for Business Card

Name: Gergely Halmindo
Email: g.halmindo@braskpartnera.hu
Web: www.braskpartnera.hu
Mobile: +36 30 555 0192
Title: Managing Director

Optional:
Company name: Brask and Partners Ltd.
Address: 1047 Budapest, Ravaszi str. 17/B, Hungary

Font styles to use
Other font styles liked:
• helveticaneue_medium, Prime Regular are used now.

Colors

Designer to choose colors to be used in the design.

Requirements
Must have
• I would like to have a 2 sided design.
Nice to have
• I thought if we make the logo a bit bigger (without the company name), that could go to the back with the company name below. I though, if the pipe in the logo is somehow touchable on the business card, would be nice and unique.

```html
<!DOCTYPE html>
<html lang="en">
<head>
<meta charset="utf-8">
<title>Brask and Partners – Business Card</title>
<link rel="stylesheet" href="https://fonts.googleapis.com/css2?family=Roboto:wght@300;400&display=swap">
<style>
  :root {
    --backdrop: #1a1a1b;
    --card: #232325;
    --ink: #e9e9ea;
    --accent: #1e90d2;
    --divider: rgba(30, 144, 210, 0.55);
  }
  * { box-sizing: border-box; margin: 0; padding: 0; }
  html, body {
    width: 1200px;
    height: 720px;
    overflow: hidden;
    background: var(--backdrop);
    font-family: "Roboto", Arial, sans-serif;
  }
  .business-card {
    position: absolute;
    left: 150px;
    top: 103px;
    width: 900px;
    height: 514px;
    background: var(--card);
    border-bottom: 4px solid var(--accent);
    color: var(--ink);
  }
  .brand-side {
    position: absolute;
    left: 0;
    top: 0;
    width: 520px;
    height: 100%;
    display: flex;
    align-items: center;
    justify-content: center;
  }
  .company-name {
    font-size: 36px;
    font-weight: 400;
    color: var(--ink);
    letter-spacing: 0.3px;
    margin-top: 90px;
    white-space: nowrap;
  }
  .divider {
    position: absolute;
    left: 520px;
    top: 40px;
    bottom: 40px;
    width: 1px;
    background: var(--divider);
  }
  .contact-side {
    position: absolute;
    left: 565px;
    top: 130px;
    right: 30px;
  }
  .person-name {
    font-size: 26px;
    font-weight: 400;
    color: var(--ink);
  }
  .person-title {
    font-size: 17px;
    font-weight: 400;
    color: var(--accent);
    margin-top: 4px;
  }
  .contact-list {
    list-style: none;
    margin-top: 34px;
  }
  .contact-item {
    display: flex;
    align-items: flex-start;
    gap: 12px;
    font-size: 18px;
    font-weight: 300;
    line-height: 26px;
    color: var(--ink);
    white-space: nowrap;
  }
  .contact-icon {
    flex: none;
    width: 18px;
    height: 18px;
    margin-top: 4px;
    fill: none;
    stroke: var(--accent);
    stroke-width: 1.6;
  }
  .contact-icon.solid { fill: var(--accent); stroke: none; }
</style>
</head>
<body>
  <article class="business-card">
    <section class="brand-side">
      <p class="company-name">Brask and Partners</p>
    </section>

    <div class="divider"></div>

    <section class="contact-side">
      <h1 class="person-name">Gergely Halmindo</h1>
      <p class="person-title">Managing Director</p>
      <ul class="contact-list">
        <li class="contact-item">
          <svg class="contact-icon" viewBox="0 0 18 18"><rect x="4.5" y="1" width="9" height="16" rx="1.5"/><line x1="8" y1="14.5" x2="10" y2="14.5"/></svg>
          <span>+36 30 555 0192</span>
        </li>
        <li class="contact-item">
          <svg class="contact-icon" viewBox="0 0 18 18"><rect x="1.5" y="3.5" width="15" height="11"/><polyline points="1.5,3.5 9,10 16.5,3.5"/></svg>
          <span>g.halmindo@braskpartnera.hu</span>
        </li>
        <li class="contact-item">
          <svg class="contact-icon" viewBox="0 0 18 18"><circle cx="9" cy="9" r="7.5"/><ellipse cx="9" cy="9" rx="3.2" ry="7.5"/><line x1="1.5" y1="9" x2="16.5" y2="9"/></svg>
          <span>www.braskpartnera.hu</span>
        </li>
        <li class="contact-item">
          <svg class="contact-icon solid" viewBox="0 0 18 18"><path d="M9 1a5.5 5.5 0 0 0-5.5 5.5C3.5 11 9 17 9 17s5.5-6 5.5-10.5A5.5 5.5 0 0 0 9 1zm0 7.8a2.3 2.3 0 1 1 0-4.6 2.3 2.3 0 0 1 0 4.6z"/></svg>
          <span>1047 Budapest,<br>Ravaszi str. 17/B, Hungary</span>
        </li>
      </ul>
    </section>
  </article>
</body>
</html>
```